Business Card - high end, modern health care

Hey designers!

We need a double sided business card for the boutique, cutting edge physical therapy rehabilitation centre in Sydney's Northern Beaches.

With the most qualified physios in the area The Harbourline Motion Clinic does what other physiotherapy practices do not, we take our time with our patients giving them longer appointments, better physios and therefor faster results!

We guarantee that the service people receive at THMC will be unparalleled.

Hence we need a business card to reflect our modern, boutique, high end service. The final design needs to reflect that we are in a class of our own yet with the feel of beachside retreat.

Below I have attached our logo in both blue on white and white on blue. The exact colour is;
and the font that we have used in our logo is Tex Gyre Aventador.

I like the idea of the blue as the main colour as it is more eye catching and our signage onto the main road will be in this blue and in the interest of consistency across marketing the blue needs to be a part of the design. However I would appreciate a few designs onto a wooden background as this is a visual theme within the fitout of the practice.

The design needs to be of standard size (91x55mm).

Target Market(s)

We target people who have an end outcome in mind and those who have had poor experiences with other providers and ensure that everyone gets the care that they deserve with a premium service that is tailored to the individuals circumstances. As a premium service, the target market is highly educated, business and tech savvy with the additional target market of elderly people who have self funded their retirement and see value in paying for the best ongoing rehabilitation to maintain independence.

Industry/Entity Type

Physical Therapy

Contact Information for Business Card

Name, designation( Titled Musculoskeletal Physiotherapist... there will also be those in the company that have multiple designations ie 5 or 6 words long), phone number, email, facebook, instagram, address

Font styles to use
Sans Serif

Colors

Designer to choose colors to be used in the design.

Requirements
Must have
• Front - The logo as large as possible, blue or wooden theme, and all of the important details.
• Back - A blank space/lines on which to write appointment times (no "Appointment, date, time" etc.)
Nice to have
• facebook url
• logos for facebook and instagram
• Mini logos for the phone and email?

```html
<!DOCTYPE html>
<html lang="en">
<head>
<meta charset="utf-8">
<title>The Harbourline Motion Clinic – Business Card</title>
<link href="https://fonts.googleapis.com/css2?family=Questrial&display=swap" rel="stylesheet">
<style>
  :root {
    --brand-blue: #1a5ce6;
    --card-white: #f6f7f6;
    --backdrop: #e3e5e4;
    --line-blue: #2a66e8;
  }
  * { margin: 0; padding: 0; box-sizing: border-box; }
  html, body { width: 1200px; height: 1010px; overflow: hidden; }
  body {
    background: var(--backdrop);
    font-family: "Questrial", "Century Gothic", sans-serif;
    color: var(--brand-blue);
    position: relative;
  }
  .card {
    position: absolute;
    left: 240px;
    width: 720px;
    height: 435px;
    background: var(--card-white);
    box-shadow: 0 2px 6px rgba(0,0,0,0.12);
    overflow: hidden;
  }
  .card--back { top: 40px; }
  .card--front { top: 535px; }

  /* Brand lockup */
  .brand { position: absolute; display: flex; align-items: center; }
  .brand__mark { border-radius: 50%; background: var(--brand-blue); flex: none; }
  .brand__name { text-transform: uppercase; line-height: 1.1; white-space: nowrap; }

  .card--back .brand { left: 50%; bottom: 40px; transform: translateX(-50%); gap: 10px; }
  .card--back .brand__mark { width: 38px; height: 38px; }
  .card--back .brand__name { font-size: 17px; letter-spacing: 1.5px; }

  .card--front .brand__mark--large {
    position: absolute; left: 48px; top: 40px; width: 270px; height: 270px;
  }
  .card--front .brand__name--large {
    position: absolute; left: 44px; top: 336px;
    font-size: 22px; letter-spacing: 2px; line-height: 1.25;
  }

  /* Person */
  .person { position: absolute; right: 40px; top: 40px; text-align: right; width: 380px; }
  .person__name { font-size: 46px; letter-spacing: 0.5px; line-height: 1; }
  .person__rule { height: 2px; background: var(--line-blue); margin: 10px 0 8px 18px; }
  .person__title { font-size: 13px; }

  /* Contacts */
  .contacts { position: absolute; right: 40px; top: 168px; width: 420px; list-style: none; }
  .contact { display: flex; justify-content: flex-end; align-items: center; gap: 22px; margin-bottom: 22px; font-size: 17px; }
  .contact__text { text-align: right; line-height: 1.3; }
  .contact__icon { width: 40px; height: 34px; flex: none; display: flex; justify-content: center; }
  .contact__icon svg { fill: var(--brand-blue); }

  /* Social */
  .social { position: absolute; right: 40px; bottom: 44px; display: flex; gap: 20px; font-size: 10.5px; }
  .social__item { display: flex; align-items: center; gap: 7px; white-space: nowrap; }
  .social__dot { width: 22px; height: 22px; border: 1.5px solid var(--brand-blue); border-radius: 50%; flex: none; }
</style>
</head>
<body>

  <section class="card card--back" aria-label="Card back">
    <div class="brand">
      <span class="brand__mark"></span>
      <span class="brand__name">The Harbourline<br>Motion Clinic</span>
    </div>
  </section>

  <section class="card card--front" aria-label="Card front">
    <span class="brand__mark brand__mark--large"></span>
    <div class="brand__name brand__name--large">The Harbourline<br>Motion Clinic</div>

    <div class="person">
      <div class="person__name">Mark Ellison</div>
      <div class="person__rule"></div>
      <div class="person__title">Titled Musculoskeletal Physiotherapist</div>
    </div>

    <ul class="contacts">
      <li class="contact">
        <span class="contact__text">+61 2 5550 1847</span>
        <span class="contact__icon">
          <svg width="30" height="32" viewBox="0 0 24 24" aria-hidden="true"><path d="M6.6 10.8a15.1 15.1 0 0 0 6.6 6.6l2.2-2.2a1 1 0 0 1 1-.25 11.4 11.4 0 0 0 3.6.57 1 1 0 0 1 1 1V20a1 1 0 0 1-1 1A17 17 0 0 1 3 4a1 1 0 0 1 1-1h3.5a1 1 0 0 1 1 1c0 1.25.2 2.45.57 3.57a1 1 0 0 1-.25 1z"/></svg>
        </span>
      </li>
      <li class="contact">
        <span class="contact__text">mark@harbourlinemotion.com</span>
        <span class="contact__icon">
          <svg width="40" height="28" viewBox="0 0 40 28" aria-hidden="true"><path d="M0 0h40v28H0z M3 3l17 13L37 3z" fill-rule="evenodd"/></svg>
        </span>
      </li>
      <li class="contact">
        <span class="contact__text">14 - 16 Tallow St,<br>Seabright NSW 2099</span>
        <span class="contact__icon">
          <svg width="26" height="38" viewBox="0 0 24 36" aria-hidden="true"><path d="M12 0a12 12 0 0 0-12 12c0 9 12 24 12 24s12-15 12-24A12 12 0 0 0 12 0zm0 17a5 5 0 1 1 0-10 5 5 0 0 1 0 10z"/></svg>
        </span>
      </li>
    </ul>

    <div class="social">
      <span class="social__item"><span class="social__dot"></span>The Harbourline Motion Clinic</span>
      <span class="social__item"><span class="social__dot"></span>harbourlinemotionclinic</span>
    </div>
  </section>

</body>
</html>
```